MMA fitness boot camp

We need a flyer that feels friendly and inviting to people who have never done fitness or training before. It also needs to look serious so it has the look of being a serious workout program.

We dont mind how it is set out as long as it conveys the message.

We do not want images of professional MMA fighters fighting. We like fitness training images that are relatable. eg- fit women punching or kicking a punching bag . If possible add men as well. We are aiming for men and women to do the boot camp.

The information for flyer is as below-

‘MMA Fitness Bootcamp’

Join us at Ironleaf Combat Studio for our new Mixed Martial Arts Bootcamp. You will train for 4 weeks with the same fitness methods a professional fighter would use before a fight! You will get an intense and challenging workout whilst having fun. This isn’t your common boot camp held at the local park, this is unique and enjoyable!

During this 4 week period, you will be training twice a week early mornings in our Training facility.

Enjoy training in a supportive environment with an MMA fighter and qualified Master trainer pushing you every session so that you get the best out of yourself.

For more information email us at marcus@ironleafcombatstudio.com.au or to book your spot with us.

or visit us at-
www.ironleafcombatstudio.com

ALL FITNESS LEVELS WELCOME!

Level 1, 274 Penrow Rd. Smithfield.'

```html
<!DOCTYPE html>
<html lang="en">
<head>
<meta charset="utf-8">
<title>MMA Fitness Bootcamp – Ironleaf Combat Studio</title>
<link rel="stylesheet" href="https://fonts.googleapis.com/css2?family=Bebas+Neue&family=Open+Sans:wght@400;600;700&display=swap">
<style>
  :root {
    --ink: #ffffff;
    --night: #141414;
    --charcoal: #2a2a2a;
    --ember: #e8452a;
    --flame: #f26a3c;
    --crimson: #c9281c;
    --amber: #f7941d;
    --glove: #c8261c;
    --skin: #8a6a58;
  }
  * { margin: 0; padding: 0; box-sizing: border-box; }
  html, body { width: 1200px; height: 2521px; overflow: hidden; background: var(--night); }
  .flyer {
    position: relative;
    width: 1200px;
    height: 2521px;
    overflow: hidden;
    background: radial-gradient(ellipse at 50% 55%, #3a3a3a 0%, var(--charcoal) 35%, var(--night) 80%);
    font-family: "Open Sans", Arial, sans-serif;
    color: var(--ink);
  }
  .hero-photo {
    position: absolute;
    left: 0; top: 0;
    width: 1200px; height: 1010px;
    background:
      linear-gradient(180deg, rgba(20,20,20,0) 78%, rgba(20,20,20,1) 100%),
      radial-gradient(ellipse 26% 30% at 33% 24%, var(--glove) 0%, rgba(200,38,28,0.75) 40%, rgba(120,18,12,0) 100%),
      radial-gradient(ellipse 40% 60% at 78% 38%, var(--skin) 0%, rgba(110,80,64,0.7) 40%, rgba(40,30,26,0) 100%),
      linear-gradient(90deg, #0a0a0a 0%, #1c1815 55%, #2e2420 100%);
  }
  .title-band {
    position: absolute;
    left: -60px; top: 938px;
    width: 1320px; height: 190px;
    transform: rotate(-5.5deg);
    background: linear-gradient(90deg, var(--crimson) 0%, var(--ember) 45%, var(--flame) 100%);
    border-top: 8px solid rgba(255,140,90,0.55);
    border-bottom: 8px solid rgba(140,20,10,0.6);
    box-shadow: 0 14px 30px rgba(0,0,0,0.55);
    display: flex; align-items: center; justify-content: center;
  }
  .title {
    font-family: "Bebas Neue", Impact, sans-serif;
    font-weight: 400;
    font-size: 132px;
    letter-spacing: 2px;
    line-height: 1;
    color: var(--ink);
    text-shadow: 0 4px 8px rgba(0,0,0,0.45);
  }
  .copy {
    position: absolute;
    left: 100px; top: 1262px;
    width: 1000px;
    text-align: center;
    font-size: 33px;
    line-height: 45px;
  }
  .copy p + p { margin-top: 45px; }
  .brand {
    position: absolute;
    left: 0; top: 2010px;
    width: 1200px;
    display: flex; align-items: center; justify-content: center; gap: 26px;
  }
  .brand-square { width: 56px; height: 56px; background: var(--amber); }
  .brand-name {
    font-family: "Open Sans", Arial, sans-serif;
    font-weight: 700;
    font-size: 66px;
    color: var(--amber);
  }
  .contact {
    position: absolute;
    left: 0; top: 2285px;
    width: 1200px;
    text-align: center;
    font-size: 31px;
    line-height: 33px;
  }
  .contact .visit { margin-top: 8px; }
  .contact .web { color: var(--amber); font-weight: 700; }
  .contact .welcome { margin-top: 10px; }
</style>
</head>
<body>
  <main class="flyer">
    <div class="hero-photo" role="img" aria-label="Photo of a woman in red boxing gloves holding a guard stance against a dark background"></div>

    <div class="title-band">
      <h1 class="title">MMA FITNESS BOOTCAMP</h1>
    </div>

    <section class="copy">
      <p>Join us at Ironleaf Combat Studio for our new Mixed Martial Arts Bootcamp. You will train for 4 weeks with the same fitness methods a professional fighter would use before a fight! You will get an intense and challenging workout whilst having fun. This isn’t your common boot camp held at the local park, this is unique and enjoyable!</p>
      <p>During this 4 week period, you will be training twice a week early mornings in our Training facility.</p>
      <p>Enjoy training in a supportive environment with an MMA fighter and qualified Master trainer pushing you every session so that you get the best out of yourself.</p>
    </section>

    <div class="brand">
      <span class="brand-square"></span>
      <span class="brand-name">Ironleaf Combat Studio</span>
    </div>

    <footer class="contact">
      <p>For more information email us at<br>marcus@ironleafcombatstudio.com.au<br>or to book your spot with us.</p>
      <p class="visit">or visit us at- <span class="web">www.ironleafcombatstudio.com</span></p>
      <p class="welcome">ALL FITNESS LEVELS WELCOME!<br>Level 1, 274 Penrow Rd. Smithfield.’</p>
    </footer>
  </main>
</body>
</html>
```